Zielgruppe
Ich bin Autorin und Verlegerin. Es geht um das Cover für ein neues Buch zum Thema 'Online-PR'. Zielgruppe des Buches sind Anwender des Online-Marketings, wie z.B. Selbständige, kleine und mittlere Unternehmen.
Aufgabenstellung
Das Buch wird der 1. Band einer Buchreihe mit dem Titel 'Kompass Netzwerbung für Einsteiger'. Das Cover sollte daher einen Wiedererkennungswert haben - es sollte für kommende Bücher der Reihe in gewissen Dingen (z.B. Cover-Foto) leicht abwandelbar sein. Name der Autorin, Haupttitel des Buches sowie Titel der Buchreihe müssen auch im Internet bei der üblichen Verkleinerung in Thumbnail-Größe (wi bei Bücherfalke) gut lesbar sein. Benötigt wird die U1 (in 3 oder 4 verschiedenen Formaten) sowie die U4 (Buchrückseite)

```html
<!DOCTYPE html>
<html lang="de">
<head>
<meta charset="utf-8">
<title>Erfolgreiche Web-Präsenz – Buchcover</title>
<link rel="stylesheet" href="https://fonts.googleapis.com/css2?family=Barlow:wght@400;500;600;700&display=swap">
<style>
  :root {
    --stage: #ececec;
    --paper: #ffffff;
    --ink: #474747;
    --ink-soft: #3f3f3f;
    --violet: #7a2a8c;
    --amber: #d9892a;
    --photo-warm: #b88a6a;
    --photo-light: #e7e3dc;
    --photo-green: #7f9a6a;
  }
  * { box-sizing: border-box; margin: 0; padding: 0; }
  html, body {
    width: 900px;
    height: 1200px;
    overflow: hidden;
    background: var(--stage);
    font-family: "Barlow", Arial, sans-serif;
  }
  .cover {
    position: absolute;
    left: 80px;
    top: 45px;
    width: 740px;
    height: 1110px;
    background: var(--paper);
    box-shadow: 0 2px 10px rgba(0,0,0,0.12);
    overflow: hidden;
  }
  .publisher {
    position: absolute;
    left: 43px;
    top: 64px;
    font-size: 24px;
    font-weight: 600;
    color: var(--violet);
    white-space: nowrap;
  }
  .author {
    position: absolute;
    right: 68px;
    top: 56px;
    font-size: 42px;
    font-weight: 400;
    color: var(--ink-soft);
    letter-spacing: 0.2px;
    white-space: nowrap;
  }
  .series-rule {
    position: absolute;
    left: 81px;
    top: 374px;
    width: 2px;
    bottom: 0;
    background: var(--violet);
  }
  .series-band {
    position: absolute;
    left: 40px;
    top: 909px;
    width: 32px;
    bottom: 0;
    background: var(--amber);
  }
  .series-title {
    position: absolute;
    left: 40px;
    bottom: 222px;
    writing-mode: vertical-rl;
    transform: rotate(180deg);
    font-size: 27px;
    font-weight: 500;
    color: var(--ink-soft);
    white-space: nowrap;
    line-height: 32px;
  }
  .book-title {
    position: absolute;
    left: 116px;
    top: 360px;
    font-size: 89px;
    font-weight: 700;
    line-height: 94px;
    color: var(--ink);
    letter-spacing: -0.5px;
    white-space: nowrap;
  }
  .book-subtitle {
    position: absolute;
    left: 124px;
    top: 574px;
    font-size: 29px;
    font-weight: 500;
    line-height: 37px;
    color: var(--violet);
    white-space: nowrap;
  }
  .cover-photo {
    position: absolute;
    left: 130px;
    top: 684px;
    width: 406px;
    height: 324px;
    background: linear-gradient(120deg, var(--photo-warm) 0%, var(--photo-light) 45%, var(--photo-green) 75%, var(--photo-light) 100%);
  }
  .accent-bar {
    position: absolute;
    left: 553px;
    top: 973px;
    width: 187px;
    height: 35px;
    background: var(--amber);
  }
</style>
</head>
<body>
  <main class="cover">
    <p class="publisher">Lesewerk Verlag</p>
    <p class="author">Marlene Vogt</p>

    <div class="series-rule"></div>
    <div class="series-band"></div>
    <p class="series-title">Kompass Netzwerbung für Einsteiger</p>

    <h1 class="book-title">Erfolgreiche<br>Web-Präsenz.</h1>
    <p class="book-subtitle">Mehr Aufmerksamkeit und größere Wirkung<br>für Ihre Leistungen im Netz</p>

    <div class="cover-photo" role="img" aria-label="Foto: zwei Geschäftsleute klatschen sich im Büro am Besprechungstisch mit Laptop ab"></div>
    <div class="accent-bar"></div>
  </main>
</body>
</html>
```